Animal care facility (Pet Grooming, Doggie daycare, Boarding, Pet Boutique)

Hi there! i came across your wonderful work and would love to work with you! I have a clear image in my head that i want for my bussiness card and stationary. I will go ahead and attach pictures of business cards that i have found to give you an idea of what i would like to see.

My color scheme is a gray back ground and white lettering. So for the card i would like it to be a gray and the logo on the front to be white and done like picture #1. I would like the quality of the card to be a thicker more durable look. I would want just my logo and then underneath my name ( Marisa Thornbury and my title Owner similar to picture #1. I also have somone i am working with so his would need to be (Colin Pratt, General Manager)

Also there is certain information that does need to be on the back of the card so I don't know if a white back with gray lettering would help it be easily read or not.

Alderwick Pet Haven & Spa LLC
862 E. Millrace Rd.
507.264.1193 -Phone
507.268.4410-Fax
Info@alderwickpethavenandspa.com-Email

Grooming- Boarding-Daycare-Pet Boutique

$10.00 OFF First Time Grooming Visit

The font for all of this is using (oranienbaum)
next to the phone fax, email I would like the actual small pictures that I have in one of the photos
Updates

Industry/Entity Type

Pet Care

Requirements
Must have
• Please follow the design of picture 7 I would like to change the direction of the card all together now. I would like the image to be up top and the name and title to be laid out the same and also in the same font as the attached picture. Again I would like all of this on the front to be engraved In white foil on gray matte backing and if we could lighten the color of this card up I would appreciate it but be on the darker side.
• On the back side keep the version you made and flip all the information to be laid out vertically just like the front.

```html
<!DOCTYPE html>
<html lang="en">
<head>
<meta charset="utf-8">
<title>Alderwick Pet Haven &amp; Spa — Business Cards</title>
<link href="https://fonts.googleapis.com/css2?family=Oranienbaum&display=swap" rel="stylesheet">
<style>
  :root {
    --backdrop: #414143;
    --card: #ffffff;
    --ink: #1f1f1f;
    --ink-soft: #2b2b2b;
    --rule: #333333;
  }
  html, body {
    margin: 0;
    padding: 0;
    width: 1200px;
    height: 913px;
    overflow: hidden;
    background: var(--backdrop);
  }
  .canvas {
    position: relative;
    width: 1200px;
    height: 913px;
    font-family: "Oranienbaum", Georgia, serif;
    color: var(--ink);
  }
  .card {
    position: absolute;
    top: 192px;
    width: 296px;
    height: 478px;
    background: var(--card);
  }
  .card--owner { left: 110px; }
  .card--manager { left: 439px; }
  .card--back { left: 791px; }

  .brand {
    position: absolute;
    left: 0;
    right: 0;
    text-align: center;
  }
  .brand__seal {
    display: block;
    margin: 0 auto;
    border-radius: 50%;
    background: var(--ink-soft);
  }
  .brand__name {
    display: block;
    color: var(--ink);
    line-height: 1;
    letter-spacing: 0.5px;
  }
  .card--owner .brand,
  .card--manager .brand { top: 80px; }
  .card--owner .brand__seal,
  .card--manager .brand__seal { width: 96px; height: 96px; margin-bottom: 28px; }
  .card--owner .brand__name,
  .card--manager .brand__name { font-size: 26px; }
  .card--owner .brand__name + .brand__name,
  .card--manager .brand__name + .brand__name { font-size: 26px; margin-top: 8px; }

  .card--back .brand { top: 48px; }
  .card--back .brand__seal { width: 56px; height: 56px; margin-bottom: 16px; }
  .card--back .brand__name { font-size: 17px; }
  .card--back .brand__name + .brand__name { margin-top: 5px; }

  .person {
    position: absolute;
    left: 0;
    right: 0;
    top: 372px;
    text-align: center;
  }
  .person__name {
    margin: 0;
    font-size: 23px;
    font-weight: 400;
    letter-spacing: 0.6px;
    line-height: 1;
    text-transform: uppercase;
  }
  .person__title {
    margin: 18px 0 0;
    font-size: 13px;
    letter-spacing: 0.4px;
    text-transform: uppercase;
  }

  .services {
    position: absolute;
    left: 0;
    right: 0;
    top: 221px;
    text-align: center;
    font-size: 12.5px;
    line-height: 20px;
    letter-spacing: 0.2px;
  }
  .services p { margin: 0; }
  .services__offer { text-transform: uppercase; font-size: 12px; }

  .contact {
    position: absolute;
    left: 62px;
    width: 168px;
    text-align: center;
    font-size: 12.5px;
  }
  .contact__divider {
    display: flex;
    align-items: center;
    height: 14px;
  }
  .contact__divider::before,
  .contact__divider::after {
    content: "";
    flex: 1;
    height: 1px;
    background: var(--rule);
  }
  .contact__icon {
    width: 12px;
    height: 12px;
    margin: 0 7px;
    fill: var(--ink);
  }
  .contact__value {
    margin: 4px 0 0;
    line-height: 14px;
  }
  .contact--address { top: 299px; }
  .contact--phone { top: 339px; }
  .contact--fax { top: 378px; }
  .contact--email { top: 415px; left: 52px; width: 188px; }
</style>
</head>
<body>
<main class="canvas">

  <section class="card card--owner" aria-label="Business card front, owner">
    <div class="brand">
      <span class="brand__seal" role="img" aria-label="Company mark area"></span>
      <span class="brand__name">ALDERWICK PET</span>
      <span class="brand__name">HAVEN &amp; SPA</span>
    </div>
    <div class="person">
      <h2 class="person__name">Marisa Thornbury</h2>
      <p class="person__title">Owner</p>
    </div>
  </section>

  <section class="card card--manager" aria-label="Business card front, general manager">
    <div class="brand">
      <span class="brand__seal" role="img" aria-label="Company mark area"></span>
      <span class="brand__name">ALDERWICK PET</span>
      <span class="brand__name">HAVEN &amp; SPA</span>
    </div>
    <div class="person">
      <h2 class="person__name">Colin Pratt</h2>
      <p class="person__title">General Manager</p>
    </div>
  </section>

  <section class="card card--back" aria-label="Business card back">
    <div class="brand">
      <span class="brand__seal" role="img" aria-label="Company mark area"></span>
      <span class="brand__name">ALDERWICK PET</span>
      <span class="brand__name">HAVEN &amp; SPA</span>
    </div>

    <div class="services">
      <p>Grooming | Boarding | Daycare | Pet Boutique</p>
      <p class="services__offer">$10.00 Off First Time Grooming Visit</p>
    </div>

    <div class="contact contact--address">
      <div class="contact__divider">
        <svg class="contact__icon" viewBox="0 0 12 12" aria-hidden="true"><path d="M6 0a4 4 0 0 0-4 4c0 3 4 8 4 8s4-5 4-8a4 4 0 0 0-4-4zm0 5.6A1.6 1.6 0 1 1 6 2.4a1.6 1.6 0 0 1 0 3.2z"/></svg>
      </div>
      <p class="contact__value">862 E. Millrace Rd.</p>
    </div>

    <div class="contact contact--phone">
      <div class="contact__divider">
        <svg class="contact__icon" viewBox="0 0 12 12" aria-hidden="true"><path d="M1 3.5C1 2.5 3 1.5 6 1.5s5 1 5 2v1H8.5v-1h-5v1H1z"/><path d="M3 6l1-1.5h4L9 6v4.5H3z"/></svg>
      </div>
      <p class="contact__value">507.264.1193</p>
    </div>

    <div class="contact contact--fax">
      <div class="contact__divider">
        <svg class="contact__icon" viewBox="0 0 12 12" aria-hidden="true"><path d="M3 1h6v3H3z"/><path d="M1 4.5h10v5H9V7.5H3v2H1z"/><path d="M3.5 8h5v3h-5z"/></svg>
      </div>
      <p class="contact__value">507.268.4410</p>
    </div>

    <div class="contact contact--email">
      <div class="contact__divider">
        <svg class="contact__icon" viewBox="0 0 12 12" aria-hidden="true"><path d="M0.5 2.5h11v7h-11z M1.2 3L6 6.8 10.8 3" fill="none" stroke="#1f1f1f" stroke-width="1"/><path d="M0.5 2.5h11L6 6.5z"/></svg>
      </div>
      <p class="contact__value">Info@alderwickpethavenandspa.com</p>
    </div>
  </section>

</main>
</body>
</html>
```